IT Company dealing Business to Business website

Built on Wordpress
Professional eye-catching website, mobile friendly and responsive
We are currently in the process of re branding the company and refreshing the current image. The current website contains the necessary information about the company and services we provide. Also detailing companies we partner with.
We have a new logo and tag line which we are eager to incorporate into the new website.
We wish to have a fresh elegant business website which reflects our company value and delivers vital information for both old and new clients about what we provide in terms of service.
The website should be an extension of our offline media and an integrated company overview.

Target Market(s)

Businesses who require IT services

Industry/Entity Type

It Company

Coding

Coded - Design and coding required

Number of Pages Required

5+ page

Font styles to use
Sans Serif

Colors

Designer to choose colors to be used in the design.

Requirements
Must have
• Be made in Wordpress, and editable after without needing coding
• Mobile friendly/responsive
• Remote links to be displayed at the top of the web page
• Pay account and customer portal also displayed at the top of the web page
• Partners of the company to be displayed at the bottom of the screen
Nice to have
• Scrolling image in the centre, to be used for advertising services/features

```html
<!DOCTYPE html>
<html lang="en">
<head>
<meta charset="utf-8">
<title>Nexora Solutions – IT Services</title>
<link href="https://fonts.googleapis.com/css2?family=Montserrat:wght@400;600;700;800&family=Open+Sans:wght@400;600&display=swap" rel="stylesheet">
<style>
:root{
  --blue:#1c63c7;
  --blue-dark:#0f3f8c;
  --navy:#0b1a2e;
  --navy-2:#071222;
  --ink:#1d1d1f;
  --muted:#8a8f98;
  --line:#dfe3ea;
  --grey:#f1f2f4;
  --white:#ffffff;
}
*{box-sizing:border-box;margin:0;padding:0}
html,body{width:1200px;height:4672px;overflow:hidden}
body{font-family:"Open Sans",Arial,sans-serif;color:var(--ink);background:var(--white);position:relative}
h1,h2,h3,h4,.brand,.btn,.nav a{font-family:"Montserrat",Arial,sans-serif}
.abs{position:absolute}
section,header,footer{position:absolute;left:0;width:1200px}
.sec-title{font-size:34px;font-weight:800;text-align:center;color:var(--ink)}
.sec-title span{color:var(--blue)}
.btn{display:inline-block;border:2px solid var(--blue);color:var(--blue);border-radius:30px;font-size:13px;font-weight:700;padding:12px 30px;letter-spacing:.5px;background:var(--white)}

/* header */
.site-header{top:0;height:70px;border-top:5px solid var(--blue);background:var(--white);box-shadow:0 2px 6px rgba(0,0,0,.08);z-index:2}
.brand{position:absolute;left:100px;top:14px;display:flex;align-items:center;gap:10px;font-size:26px;font-weight:800;color:var(--blue-dark);letter-spacing:1px}
.brand i{width:28px;height:28px;background:var(--blue);border-radius:4px;display:block}
.nav{position:absolute;right:100px;top:22px;display:flex;gap:28px;align-items:center}
.nav a{font-size:14px;font-weight:600;color:var(--ink);text-decoration:none}
.nav .pay{background:var(--blue);color:var(--white);padding:8px 18px;border-radius:20px;margin-top:-6px}

/* hero */
.hero{top:70px;height:670px;background:linear-gradient(100deg,#2c3544 0%,#3d4a5c 40%,#1c5cc0 55%,#1550b0 100%);overflow:hidden}
.hero-photo{position:absolute;left:0;top:0;width:700px;height:670px;background:linear-gradient(120deg,#6d7d91,#3a4758 60%,#2a3341);clip-path:polygon(0 0,100% 0,78% 100%,0 100%)}
.hero h1{position:absolute;left:640px;top:230px;font-size:46px;font-weight:800;color:var(--white);letter-spacing:1px}
.hero p{position:absolute;left:640px;top:292px;width:430px;color:#dbe6f7;font-size:14px;line-height:1.6}
.hero .btn{position:absolute;left:950px;top:370px;background:transparent;color:var(--white);border-color:var(--white);padding:10px 22px;font-size:12px}
.dots{position:absolute;left:570px;top:620px;display:flex;gap:8px}
.dots b{width:10px;height:10px;border-radius:50%;background:rgba(255,255,255,.5)}
.dots b:first-child{background:var(--white)}

/* about */
.about{top:740px;height:660px}
.about h2{position:absolute;left:100px;top:140px;font-size:30px;font-weight:800;line-height:1.25}
.about h2 span{color:var(--blue)}
.about p{position:absolute;left:100px;top:240px;width:420px;color:var(--muted);font-size:14px;line-height:1.8}
.about .btn{position:absolute;left:100px;top:480px}
.about-frame{position:absolute;left:575px;top:130px;width:520px;height:395px;border:2px solid var(--blue)}
.about-video{position:absolute;left:595px;top:150px;width:505px;height:390px;background:linear-gradient(135deg,#1b2f4d,#0d1a2c 60%,#24466f)}
.play{position:absolute;left:820px;top:310px;width:64px;height:64px;border-radius:50%;background:rgba(255,255,255,.85)}
.play:after{content:"";position:absolute;left:26px;top:20px;border-left:18px solid var(--blue);border-top:12px solid transparent;border-bottom:12px solid transparent}

/* services */
.services{top:1400px;height:740px;background:var(--grey)}
.services .sec-title{position:absolute;top:120px;width:100%}
.svc{position:absolute;width:300px;display:flex;gap:18px}
.svc .ic{flex:none;width:60px;height:60px;border-radius:50%;border:2px solid var(--blue);display:flex;align-items:center;justify-content:center;background:var(--white)}
.svc h4{font-size:13px;font-weight:700;margin-top:6px;margin-bottom:6px}
.svc p{font-size:12px;color:var(--muted);line-height:1.6}
.services .btn{position:absolute;left:495px;top:570px}

/* products */
.products{top:2140px;height:630px}
.products .sec-title{position:absolute;top:120px;width:100%}
.prod{position:absolute;top:230px;width:215px;height:280px;background:var(--white);box-shadow:0 3px 10px rgba(0,0,0,.12)}
.prod .ph{height:180px}
.prod h4{font-size:15px;font-weight:600;margin:20px 14px 6px}
.prod p{font-size:12px;color:var(--muted);margin:0 14px}
.arrow{position:absolute;top:345px;width:32px;height:32px;border-radius:50%;background:var(--white);border:1px solid var(--line);display:flex;align-items:center;justify-content:center}

/* blog */
.blog{top:2770px;height:710px;background:var(--grey)}
.blog .sec-title{position:absolute;top:110px;width:100%}
.post{position:absolute;top:210px;width:320px;height:290px;background:var(--white);box-shadow:0 3px 10px rgba(0,0,0,.1)}
.post .ph{height:200px}
.post .avatar{position:absolute;right:14px;top:180px;width:44px;height:44px;border-radius:50%;background:#c9b39a;border:3px solid var(--white)}
.post h4{font-size:14px;font-weight:600;margin:22px 16px 6px}
.post p{font-size:11px;color:var(--muted);margin:0 16px;line-height:1.5}
.post .meta{display:flex;justify-content:space-between;font-size:10px;color:var(--muted);margin:10px 16px 0}
.post .meta b{color:var(--blue);font-weight:700}

/* news */
.news{top:3480px;height:510px}
.news .sec-title{position:absolute;top:140px;width:100%}
.item{position:absolute;top:225px;display:flex;gap:22px;width:490px}
.item .ph{flex:none;width:160px;height:130px}
.item h4{font-size:15px;font-weight:600;margin-bottom:6px}
.item small{display:block;font-size:10px;color:var(--blue);margin-bottom:8px}
.item p{font-size:12px;color:var(--muted);line-height:1.6}

/* partners */
.partners{top:3990px;height:145px;background:var(--grey)}
.badge{position:absolute;top:30px;width:220px;height:80px;background:var(--white);border-radius:4px;display:flex;align-items:center;justify-content:center}
.badge i{display:block;width:110px;height:26px;border-radius:13px;background:#d6dbe3}

/* newsletter */
.newsletter{top:4135px;height:105px;background:var(--blue)}
.newsletter h3{position:absolute;left:100px;top:34px;font-size:30px;font-weight:700;color:var(--white)}
.field{position:absolute;left:478px;top:36px;width:490px;height:40px;border-radius:20px;background:var(--white);font-size:12px;color:var(--muted);padding:12px 22px}
.newsletter .btn{position:absolute;left:945px;top:36px;background:var(--navy);color:var(--white);border-color:var(--navy);padding:11px 28px}

/* footer */
.site-footer{top:4240px;height:400px;background:var(--navy);color:#c9d2df}
.col{position:absolute;top:40px}
.col h4{font-size:13px;font-weight:700;color:var(--white);margin-bottom:20px;letter-spacing:.5px}
.col li{list-style:none;font-size:12px;margin-bottom:18px;display:flex;align-items:center;gap:12px}
.col .dot{width:6px;height:6px;border-radius:50%;background:#c9d2df}
.soc{width:34px;height:34px;border-radius:50%;border:1px solid #5d6b80}
.foot-brand{position:absolute;left:830px;top:40px;font-family:"Montserrat",Arial,sans-serif;font-size:26px;font-weight:800;color:var(--white);display:flex;align-items:center;gap:10px}
.foot-brand i{width:28px;height:28px;border-radius:4px;background:var(--white);display:block}
.site-footer .btn{position:absolute;left:830px;top:120px;background:transparent;border-color:var(--white);color:var(--white);padding:10px 22px;font-size:12px}
.copy{top:4640px;height:32px;background:var(--navy-2);color:#8d98a8;font-size:11px;text-align:center;line-height:32px;position:absolute;left:0;width:1200px}
</style>
</head>
<body>

<header class="site-header">
  <div class="brand"><i></i>NEXORA SOLUTIONS</div>
  <nav class="nav">
    <a>Home</a><a>IT Services ▾</a><a>Solutions</a><a>News/Blog</a><a>Contact</a><a class="pay">Pay Now</a>
  </nav>
</header>

<section class="hero">
  <div class="hero-photo" role="img" aria-label="Photo of two IT specialists working at computer screens in an office"></div>
  <h1>MAKING IT HAPPEN</h1>
  <p>We keep your business systems fast, secure and supported so your team can focus on the work that matters most every day.</p>
  <a class="btn">READ MORE</a>
  <div class="dots"><b></b><b></b><b></b><b></b></div>
</section>

<section class="about">
  <h2>About<br><span>Nexora Solutions</span></h2>
  <p>Nexora Solutions is a privately owned company operating in Perth, Western Australia. Our team of skilled staff supports small and mid sized businesses across many industries, supplying hardware, software and IT support. We value clear advice, quick response and lasting partnerships, and we keep improving the way we deliver service to every client.</p>
  <a class="btn">READ MORE</a>
  <div class="about-frame"></div>
  <div class="about-video" role="img" aria-label="Video still of a technician monitoring several server screens"></div>
  <div class="play"></div>
</section>

<section class="services">
  <h2 class="sec-title">IT <span>Services</span></h2>

  <div class="svc" style="left:100px;top:240px"><div class="ic"><svg width="28" height="28" viewBox="0 0 28 28" fill="none" stroke="#1c63c7" stroke-width="2"><rect x="3" y="5" width="22" height="14" rx="1"/><path d="M10 24h8M14 19v5"/></svg></div><div><h4>IT MANAGEMENT</h4><p>We plan, run and watch your systems so they stay stable and secure.</p></div></div>
  <div class="svc" style="left:450px;top:240px"><div class="ic"><svg width="28" height="28" viewBox="0 0 28 28" fill="#1c63c7"><circle cx="9" cy="10" r="4"/><circle cx="19" cy="10" r="4"/><path d="M2 23c0-5 3-7 7-7s7 2 7 7zM12 23c0-5 3-7 7-7s7 2 7 7z"/></svg></div><div><h4>CONSULTATIONS</h4><p>Clear advice on the right tools and plans to help your business grow.</p></div></div>
  <div class="svc" style="left:800px;top:240px"><div class="ic"><svg width="28" height="28" viewBox="0 0 28 28" fill="#1c63c7"><path d="M14 4 3 14h3v10h6v-6h4v6h6V14h3z"/></svg></div><div><h4>OFFICE RELOCATIONS</h4><p>Moving offices? We pack, shift and set up every device for you.</p></div></div>
  <div class="svc" style="left:100px;top:400px"><div class="ic"><svg width="28" height="28" viewBox="0 0 28 28" fill="none" stroke="#1c63c7" stroke-width="2"><path d="M5 17v-3a9 9 0 0 1 18 0v3"/><rect x="4" y="16" width="5" height="7" rx="1"/><rect x="19" y="16" width="5" height="7" rx="1"/></svg></div><div><h4>TELECOMMUNICATIONS</h4><p>Phone lines, internet and voice plans set up to suit your team.</p></div></div>
  <div class="svc" style="left:450px;top:400px"><div class="ic"><svg width="28" height="28" viewBox="0 0 28 28" fill="none" stroke="#1c63c7" stroke-width="2"><rect x="6" y="6" width="16" height="11" rx="1"/><path d="M3 21h22"/></svg></div><div><h4>OFFICE SETUPS</h4><p>Desks, networks and devices ready to work from the first day.</p></div></div>
  <div class="svc" style="left:800px;top:400px"><div class="ic"><svg width="28" height="28" viewBox="0 0 28 28" fill="#1c63c7"><path d="M8 3h4l2 6-3 2a14 14 0 0 0 6 6l2-3 6 2v4c0 2-2 3-4 3C12 23 5 16 5 7c0-2 1-4 3-4z"/></svg></div><div><h4>PHONE SUPPORT</h4><p>Friendly help on the phone when something stops working well.</p></div></div>

  <a class="btn">VIEW ALL SERVICES</a>
</section>

<section class="products">
  <h2 class="sec-title">Our <span>Products</span></h2>
  <div class="arrow" style="left:40px"><svg width="10" height="12"><path d="M8 1 2 6l6 5" stroke="#555" fill="none" stroke-width="2"/></svg></div>
  <div class="prod" style="left:100px"><div class="ph" role="img" aria-label="Photo of a laptop showing office apps" style="background:linear-gradient(135deg,#2d6fd0,#7cc0e8)"></div><h4>Cloud Office</h4><p>Email, files and apps in one place.</p></div>
  <div class="prod" style="left:362px"><div class="ph" role="img" aria-label="Photo of a desk phone and headset" style="background:linear-gradient(135deg,#3b4452,#9aa3ad)"></div><h4>VOIP</h4><p>Business calls over the internet.</p></div>
  <div class="prod" style="left:624px"><div class="ph" role="img" aria-label="Photo of a padlock on a blue digital background" style="background:linear-gradient(135deg,#0d2b6b,#2f7de0)"></div><h4>PlanDesk</h4><p>Mark up and share plan documents.</p></div>
  <div class="prod" style="left:886px"><div class="ph" role="img" aria-label="Photo of hands typing on a laptop" style="background:linear-gradient(135deg,#6b5a4c,#c7b29a)"></div><h4>Hardware</h4><p>Laptops, servers and network gear.</p></div>
  <div class="arrow" style="left:1128px"><svg width="10" height="12"><path d="M2 1l6 5-6 5" stroke="#555" fill="none" stroke-width="2"/></svg></div>
</section>

<section class="blog">
  <h2 class="sec-title">Our <span>Blog Posts</span></h2>
  <div class="post" style="left:100px"><div class="ph" role="img" aria-label="Photo of security icons over a dark network background" style="background:linear-gradient(135deg,#123a5c,#3d7fa8)"></div><div class="avatar" role="img" aria-label="Author avatar"></div><h4>Quis autem vel eum iure</h4><p>Simple steps to keep your office network safe from common online threats.</p><div class="meta"><span>May 2019 · 4</span><b>READ MORE</b></div></div>
  <div class="post" style="left:440px"><div class="ph" role="img" aria-label="Photo of an engineer working on a laptop" style="background:linear-gradient(135deg,#1e2a3b,#5a7ea6)"></div><div class="avatar" role="img" aria-label="Author avatar"></div><h4>Quis autem vel eum iure</h4><p>How a planned upgrade cycle saves money and avoids long periods of downtime.</p><div class="meta"><span>May 2019 · 2</span><b>READ MORE</b></div></div>
  <div class="post" style="left:780px"><div class="ph" role="img" aria-label="Photo of a team working at computers" style="background:linear-gradient(135deg,#5b4c42,#a59585)"></div><div class="avatar" role="img" aria-label="Author avatar"></div><h4>Quis autem vel eum iure</h4><p>Why moving your files to the cloud helps your staff work from anywhere.</p><div class="meta"><span>May 2019 · 6</span><b>READ MORE</b></div></div>
</section>

<section class="news">
  <h2 class="sec-title">Latest <span>News</span></h2>
  <div class="item" style="left:100px"><div class="ph" role="img" aria-label="Photo of a hooded figure at a keyboard" style="background:linear-gradient(135deg,#0b1626,#1f4f8a)"></div><div><h4>Quis nostrum exercitationem</h4><small>20 April 2019 by Admin</small><p>We have expanded our support hours so clients can reach our team earlier in the morning and later each evening.</p></div></div>
  <div class="item" style="left:630px"><div class="ph" role="img" aria-label="Photo of a person holding a tablet" style="background:linear-gradient(135deg,#3e4b5c,#9aa7b6)"></div><div><h4>Quis nostrum exercitationem</h4><small>18 April 2019 by Admin</small><p>Our new managed backup plan is now live, giving every business daily copies of files stored in a secure location.</p></div></div>
</section>

<section class="partners">
  <div class="badge" style="left:100px"><i></i></div>
  <div class="badge" style="left:362px"><i></i></div>
  <div class="badge" style="left:624px"><i></i></div>
  <div class="badge" style="left:886px"><i></i></div>
</section>

<section class="newsletter">
  <h3>Sign Up Newsletter</h3>
  <div class="field">Enter Email Address</div>
  <a class="btn">SIGN UP</a>
</section>

<footer class="site-footer">
  <div class="col" style="left:100px">
    <h4>CONTACT US</h4>
    <ul>
      <li><svg width="14" height="16" viewBox="0 0 14 16" fill="#c9d2df"><path d="M7 0a6 6 0 0 0-6 6c0 4 6 10 6 10s6-6 6-10a6 6 0 0 0-6-6zm0 8a2 2 0 1 1 0-4 2 2 0 0 1 0 4z"/></svg>PO Box 4820, Riverside<br>WA 6000</li>
      <li><svg width="14" height="14" viewBox="0 0 28 28" fill="#c9d2df"><path d="M8 3h4l2 6-3 2a14 14 0 0 0 6 6l2-3 6 2v4c0 2-2 3-4 3C12 23 5 16 5 7c0-2 1-4 3-4z"/></svg>Phone: (08) 9000 1234</li>
      <li><svg width="14" height="12" viewBox="0 0 14 12" fill="none" stroke="#c9d2df" stroke-width="1.5"><rect x="1" y="1" width="12" height="10"/><path d="m1 1 6 5 6-5"/></svg>Email: hello@nexora.example</li>
    </ul>
  </div>
  <div class="col" style="left:400px">
    <h4>QUICK LINKS</h4>
    <ul><li><i class="dot"></i>Home</li><li><i class="dot"></i>IT Services</li><li><i class="dot"></i>Solutions</li><li><i class="dot"></i>News</li><li><i class="dot"></i>Contact Us</li></ul>
  </div>
  <div class="col" style="left:610px">
    <h4>STAY CONNECTED</h4>
    <ul><li><i class="soc"></i>Friendbook</li><li><i class="soc"></i>Chirper</li><li><i class="soc"></i>Snapgram</li></ul>
  </div>
  <div class="foot-brand"><i></i>NEXORA SOLUTIONS</div>
  <a class="btn">GET IN TOUCH</a>
</footer>
<div class="copy">© copyright 2019 Nexora Solutions All Rights Reserved &nbsp;|&nbsp; Privacy policy</div>

</body>
</html>
```